Online Rug Store needs Clearance Banner

Website is: Lanternfield Carpets and Home
You can access it at: www.lanternfieldcarpetsandhome.com and login (top right) with password: trazok

*** update: When creating banners for my site, you have permission to use images from www.velbora.com, but ONLY for this project. The images/artwork are copyright allowable for use on www.lanternfieldcarpetsandhome.com projects.***

We need a home page banner sized 1000 wide x 500 tall pixels to promote a "Clearance Sale" on rugs. The banner can state:

1. Clearance Sale
2. Now in progress
3. Save an extra 20% with coupon code 'Mint20'
4. Ends March 31st
5. Plus Free Shipping and 30 day returns.

We prefer a banner that appears hand-drawn and artistic, not commercially produced. It is OK to use a room scene image, rug images, or just a colored/textured background with text and no images. Your choice.

Flat graphics with no shadows and 3-D effect preferred.
Attached is are 3 logo options, as well as an example banner with handcrafted, artistic styling that we prefer.

Target Market(s)

This should be an eye-catching banner to showcase a very urgent promotion. Consider using colors of red, white, gold, and black to make a strong statement on the home page.

Industry/Entity Type

Home And Garden

Requirements
Must have
• Winner must provide Photoshop editable file format (.psd format) including layers that can be edited.
Nice to have
• Hand-drawn, stenciled, scribbled, artistic graphics and fonts is nice because we sell rugs that are made by hand.
Should not have
• little to no shadowing. Avoid computerized graphics.

```html
<!DOCTYPE html>
<html lang="en">
<head>
<meta charset="utf-8">
<title>Lanternfield Carpets and Home – Clearance Sale Banner</title>
<link rel="stylesheet" href="https://fonts.googleapis.com/css2?family=Oswald:wght@300;400;500;600;700&display=swap">
<style>
  :root{
    --panel: rgba(20,18,17,0.86);
    --gold: #f7b21b;
    --white: #ffffff;
    --ribbon: #f2776a;
    --ribbon-fold: #b54a40;
    --ribbon-shade: #d9665b;
    --room-dark: #3a2118;
    --room-mid: #6b4a36;
    --rug-light: #cfc3a8;
    --rug-mid: #a8957a;
  }
  html,body{margin:0;padding:0;width:1200px;height:600px;overflow:hidden;background:#fff;}
  .banner{position:relative;width:1200px;height:600px;overflow:hidden;font-family:'Oswald',sans-serif;}
  .room-photo{
    position:absolute;inset:0;
    background:
      radial-gradient(ellipse 60% 40% at 60% 75%, var(--rug-light) 0%, var(--rug-mid) 45%, transparent 75%),
      linear-gradient(180deg, #5b4b3e 0%, #4a3328 28%, var(--room-mid) 45%, var(--room-dark) 100%);
  }
  .art{position:absolute;inset:0;width:1200px;height:600px;}
  .side-panel{fill:var(--panel);}
  .brand-name{font-family:'Oswald',sans-serif;font-weight:400;fill:var(--white);letter-spacing:2px;}
  .brand-mark{fill:var(--white);}
  .headline{font-family:'Oswald',sans-serif;font-weight:700;fill:var(--gold);font-size:38px;}
  .subline{font-family:'Oswald',sans-serif;font-weight:500;fill:var(--white);font-size:15px;letter-spacing:0.5px;}
  .ribbon-face{fill:var(--ribbon);}
  .ribbon-fold{fill:var(--ribbon-fold);}
  .ribbon-tail{fill:var(--ribbon-shade);}
  .ribbon-text{font-family:'Oswald',sans-serif;font-weight:700;fill:var(--white);}
  .coupon-box{fill:none;stroke:var(--white);stroke-width:1.2;stroke-dasharray:3 3;}
  .coupon-label{font-family:'Oswald',sans-serif;font-weight:600;fill:var(--white);font-size:16px;}
  .coupon-code{font-family:'Oswald',sans-serif;font-weight:700;fill:var(--gold);font-size:25px;}
  .icon{fill:var(--white);}
  .icon-line{fill:none;stroke:var(--white);stroke-width:2;}
  .shipping-text{font-family:'Oswald',sans-serif;font-weight:500;fill:var(--white);font-size:13.5px;}
</style>
</head>
<body>
<div class="banner">
  <div class="room-photo" role="img" aria-label="Living room with a sofa, a dark coffee table holding two vases, and a beige and brown patchwork rug on a wooden floor"></div>
  <svg class="art" viewBox="0 0 1000 500" xmlns="http://www.w3.org/2000/svg">
    <defs>
      <path id="headline-arc" d="M84,178 Q210,118 350,160"/>
    </defs>

    <rect class="side-panel" x="65" y="0" width="306" height="500"/>

    <g class="brand">
      <rect class="brand-mark" x="86" y="22" width="46" height="46"/>
      <text class="brand-name" x="145" y="42" font-size="24">LANTERNFIELD</text>
      <text class="brand-name" x="146" y="67" font-size="17">Carpets and Home</text>
    </g>

    <g class="sale-headline">
      <text class="headline"><textPath href="#headline-arc" startOffset="0">CLEARANCE SALE</textPath></text>
      <text class="subline" transform="rotate(-6 200 178)" x="133" y="185">NOW IN PROGRESS</text>
    </g>

    <g class="end-ribbon" transform="rotate(16 200 245)">
      <polygon class="ribbon-tail" points="100,232 118,232 118,272 100,272 110,252"/>
      <rect class="ribbon-face" x="118" y="222" width="150" height="46"/>
      <polygon class="ribbon-fold" points="248,268 268,268 268,282"/>
      <text class="ribbon-text" x="155" y="258" font-size="30">END</text>
    </g>

    <g class="date-ribbon" transform="rotate(-16 260 300)">
      <rect class="ribbon-face" x="174" y="276" width="170" height="48"/>
      <polygon class="ribbon-tail" points="344,284 372,284 360,306 372,328 344,328"/>
      <polygon class="ribbon-fold" points="174,264 194,276 174,276"/>
      <text class="ribbon-text" x="186" y="314" font-size="26">MARCH 31<tspan font-size="14" dy="-11">ST</tspan></text>
    </g>

    <g class="coupon">
      <rect class="coupon-box" x="76" y="382" width="283" height="51"/>
      <rect x="88" y="372" width="30" height="18" fill="#1d1a18"/>
      <g class="scissors" transform="translate(92 373)">
        <circle class="icon-line" cx="4" cy="4" r="3" stroke-width="1.6"/>
        <circle class="icon-line" cx="4" cy="13" r="3" stroke-width="1.6"/>
        <path class="icon-line" stroke-width="1.6" d="M6.5,6 L22,13 M6.5,11 L22,4"/>
      </g>
      <text class="coupon-label" x="95" y="416">USE COUPON CODE:</text>
      <text class="coupon-code" x="264" y="418">MINT20</text>
    </g>

    <g class="shipping">
      <g class="truck" transform="translate(80 456)">
        <rect class="icon" x="10" y="0" width="22" height="14"/>
        <path class="icon" d="M33,3 H41 L46,9 V14 H33 Z"/>
        <circle class="icon" cx="17" cy="17" r="3.5"/>
        <circle class="icon" cx="39" cy="17" r="3.5"/>
        <rect class="icon" x="0" y="3" width="8" height="2"/>
        <rect class="icon" x="2" y="8" width="6" height="2"/>
      </g>
      <text class="shipping-text" x="138" y="474">Free Shipping and 30 day returns</text>
    </g>
  </svg>
</div>
</body>
</html>
```